Create a Magazine Ad for an asbestos law firm

we need an 8 X 13 ad to be on the back of a magazine cover. We have the text Attached and want a similar look and feel to our website : www.harborvale-claims.example. The ad should be targeted to white males 55 years or older who are conservative and worked in industry or industrial plants. The main offer is a free case review and trying to get them to call the telephone number.

Target Market(s)

White collar men who worked in industrial plants. Age 55 years or older.

Industry/Entity Type

Legal

Requirements
Must have
• Pictures of white middle class conservative man or man and woman
Nice to have
• look at www.harborvale-claims.example to an. idea of what we are looking for

```html
<!DOCTYPE html>
<html lang="en">
<head>
<meta charset="utf-8">
<title>Mesothelioma Compensation – Magazine Ad</title>
<link href="https://fonts.googleapis.com/css2?family=Bebas+Neue&family=Roboto:wght@300;400;700&family=Roboto+Slab:wght@300&display=swap" rel="stylesheet">
<style>
  :root {
    --ink: #24485e;
    --ink-body: #2f5670;
    --panel-grey: #7e7f81;
    --paper: #ffffff;
    --photo-warm: #cdb49e;
    --photo-cool: #d9dadb;
  }
  * { margin: 0; padding: 0; box-sizing: border-box; }
  html, body { width: 873px; height: 1200px; overflow: hidden; background: var(--paper); }
  .ad { position: relative; width: 873px; height: 1200px; font-family: "Roboto", sans-serif; color: var(--ink-body); }

  .headline {
    position: absolute; left: 44px; top: 32px;
    font-family: "Bebas Neue", sans-serif; font-weight: 400;
    font-size: 60px; line-height: 66px; color: var(--ink); letter-spacing: 0.2px;
  }

  .hero-photo {
    position: absolute; left: 0; top: 178px; width: 873px; height: 584px;
    background: linear-gradient(100deg, var(--photo-warm) 0%, #dcc8b6 18%, #9db8d3 38%, #e7cfcc 62%, var(--photo-cool) 85%);
  }
  .hero-caption {
    position: absolute; left: 0; top: 732px; width: 412px; height: 22px;
    background: var(--paper); padding-left: 44px;
    font-weight: 700; font-size: 14px; line-height: 22px; color: var(--ink);
  }

  .offer-panel {
    position: absolute; left: 434px; top: 664px; width: 439px; height: 194px;
    background: var(--panel-grey); color: var(--paper); text-align: right; padding-right: 51px;
  }
  .offer-title {
    font-family: "Roboto Slab", serif; font-weight: 300;
    font-size: 25px; line-height: 31px; margin-top: 26px; letter-spacing: 0.3px;
  }
  .offer-text { font-weight: 300; font-size: 16px; line-height: 18.3px; margin-top: 28px; }

  .column-left { position: absolute; left: 44px; top: 780px; width: 368px; }
  .column-right { position: absolute; left: 455px; top: 868px; width: 368px; }

  .lead { font-weight: 700; font-size: 16px; line-height: 16.5px; color: var(--ink); text-align: justify; }
  .subhead { font-weight: 700; font-size: 15.5px; line-height: 16.5px; color: var(--ink); text-align: justify; }
  .body-copy { font-weight: 300; font-size: 16px; line-height: 16.7px; text-align: justify; }

  .bullets { list-style: none; font-weight: 300; font-size: 16px; line-height: 15.3px; }
  .bullets li { position: relative; padding-left: 27px; text-align: justify; }
  .bullets li::before { content: "•"; position: absolute; left: 0; font-size: 11px; }

  .results { width: 100%; border-collapse: collapse; font-weight: 300; font-size: 16px; letter-spacing: -0.4px; }
  .results td { padding: 0; line-height: 16.7px; white-space: nowrap; }
  .results td.amount { text-align: right; }
</style>
</head>
<body>
<div class="ad">
  <h1 class="headline">Diagnosed with Mesothelioma,<br>you could be owed compensation</h1>

  <div class="hero-photo" role="img" aria-label="Photo of a smiling senior couple, a grey-bearded man in a light blue sweater embracing a woman in glasses and a pink sweater, in a softly lit living room"></div>
  <div class="hero-caption">Marlow &amp; Pike, LLP, Owen Marlow, Alderbrook, TX</div>

  <div class="offer-panel">
    <p class="offer-title">FIND OUT IF YOU’RE ELIGIBLE,<br>FOR FREE, IN MINUTES.</p>
    <p class="offer-text">We’ll evaluate your situation and tell you what your<br>case could be worth.<br>Get your Free evaluation now!<br>CALL 1-XXX XXXX (good number)</p>
  </div>

  <section class="column-left">
    <p class="lead">It’s very likely you developed this disease through asbestos exposure. Mesothelioma patients are getting multi-million dollar settlements, decades later, from:</p>
    <ul class="bullets" style="margin-top:13px">
      <li>Exposure to asbestos products,</li>
      <li>Ex-employers, or</li>
      <li>Talcum baby powder companies.</li>
    </ul>
    <p class="subhead" style="margin-top:18px">We can help you find out if you qualify for a case in minutes.</p>
    <ul class="bullets" style="margin-top:14px">
      <li>We’ll analyze your situation at no cost</li>
      <li>Determine how much compensation you could be entitled too</li>
      <li>Show you the next steps to get what you’re owed</li>
    </ul>
    <table class="results" style="margin-top:10px">
      <tr><td>Exposed through heavy duty vehicles</td><td class="amount">$6,142,500</td></tr>
      <tr><td>Exposed through general contracting</td><td class="amount">$6,033,510</td></tr>
      <tr><td>Exposed through boat repair</td><td class="amount">$5,939,010</td></tr>
      <tr><td>Exposed through navy service</td><td class="amount">$3,921,750</td></tr>
      <tr><td>Exposed through navy service</td><td class="amount">$3,600,450</td></tr>
      <tr><td>Exposed from Brightwell Talcum Baby Powder</td><td class="amount">$2.5 Million</td></tr>
    </table>
  </section>

  <section class="column-right">
    <h2 class="subhead">$30 Billion is Available in Trust for Mesothelioma Patients</h2>
    <p class="body-copy" style="margin-top:9px">Tradesmen in many industries were negligently exposed to asbestos materials well into the 1990s. Whether you developed Mesothelioma yourself due to asbestos exposure or you’re the surviving family of a lost loved one you could be entitled to significant compensation.</p>
    <h2 class="subhead" style="margin-top:13px">How much Money Can People Receive from a Mesothelioma Case?</h2>
    <p class="body-copy" style="margin-top:9px; line-height:15.3px">Depending on where you were exposed and a few other factors, you can get a settlement from 6 to 7 figures. Here are a few examples of Mesothelioma Settlements received by our clients. These figures are the total compensation after all attorney fees and expenses are deducted.</p>
  </section>
</div>
</body>
</html>
```